Mission statement design for a secondary school

We have the content of our mission statement and need an appealing layout. The design should fit on a poster or A4 page. The content grouping in the document should also be graphically recognizable. Our target group are young people and their parents as well as the school staff, which is why we need a modern design that is not out after 2 years. It must be easy to grasp visually and graphically simple.

Target Market(s)

Actors of the school

Requirements
Must have
• cantonal logo including school name see document can be integrated as a header
Should not have
• References to trademarks or third parties

```html
<!DOCTYPE html>
<html lang="de">
<head>
<meta charset="utf-8">
<title>Leitbild – Sekundarschule Talberg</title>
<link rel="stylesheet" href="https://fonts.googleapis.com/css2?family=Arimo:wght@700&family=Roboto+Condensed:wght@300;400;700&family=IBM+Plex+Mono:wght@500&display=swap">
<style>
  :root {
    --red: #e30613;
    --ink: #1d1d1b;
    --paper: #ffffff;
    --photo-green: #6f9a58;
    --photo-skin: #e8b3a6;
    --photo-white: #e6e4ec;
  }
  * { margin: 0; padding: 0; box-sizing: border-box; }
  html, body { width: 849px; height: 1200px; overflow: hidden; background: var(--paper); }
  .page { position: relative; width: 849px; height: 1200px; background: var(--paper); color: var(--ink); }

  .brand { position: absolute; top: 30px; right: 41px; display: flex; align-items: flex-start; gap: 6px; }
  .brand-name { font-family: "Arimo", sans-serif; font-weight: 700; color: var(--red); font-size: 19px; line-height: 19px; letter-spacing: 1.5px; text-align: right; }
  .brand-mark { width: 10px; height: 10px; background: var(--red); margin-top: 4px; }

  .department { position: absolute; top: 79px; right: 73px; text-align: right; font-family: "IBM Plex Mono", monospace; font-weight: 500; font-size: 10.5px; line-height: 15px; letter-spacing: 0.6px; color: var(--red); text-transform: uppercase; }

  .hero-photo { position: absolute; top: 137px; left: 0; width: 849px; height: 490px;
    background:
      radial-gradient(ellipse 300px 240px at 470px 300px, var(--photo-skin), transparent 75%),
      radial-gradient(ellipse 180px 300px at 760px 260px, var(--photo-white), transparent 75%),
      linear-gradient(90deg, var(--photo-green) 0%, #9fb27e 35%, #d9b7a8 60%, #d8d6df 100%); }

  .attitude { position: absolute; top: 626px; left: 0; width: 849px; height: 134px; background: var(--red); color: var(--paper); }
  .attitude-title { position: absolute; left: 41px; top: 20px; font-family: "Arimo", sans-serif; font-weight: 700; font-size: 25px; line-height: 33px; letter-spacing: 6px; }
  .attitude-list { position: absolute; left: 442px; top: 20px; list-style: none; font-family: "Roboto Condensed", sans-serif; font-weight: 400; font-size: 18.5px; line-height: 23px; }

  .section { position: absolute; }
  .section h2 { font-family: "Arimo", sans-serif; font-weight: 700; color: var(--red); font-size: 25px; line-height: 28px; letter-spacing: 5.5px; margin-bottom: 2px; }
  .section ul { list-style: none; font-family: "Roboto Condensed", sans-serif; font-weight: 300; font-size: 15px; line-height: 22.9px; }
  .section li::before { content: "»"; display: inline-block; width: 12px; font-weight: 400; }
  .learning { left: 41px; top: 779px; }
  .development { left: 442px; top: 779px; }
  .community { left: 41px; top: 1024px; }

  .contact { position: absolute; right: 61px; top: 1073px; text-align: right; font-family: "Roboto Condensed", sans-serif; font-weight: 300; font-size: 12.5px; line-height: 18.7px; color: var(--red); }
  .contact strong { font-weight: 700; font-size: 12.5px; }
  .contact-bar { position: absolute; left: 797px; top: 1075px; width: 11px; height: 86px; background: var(--red); }
</style>
</head>
<body>
<main class="page">
  <header>
    <div class="brand">
      <div class="brand-name">KANTON<br>TALBERG</div>
      <div class="brand-mark"></div>
    </div>
    <div class="department">Bildungs-, Kultur- und Sportdirektion<br>Sekundarschule Talberg</div>
  </header>

  <div class="hero-photo" role="img" aria-label="Foto: Jugendliche liegt entspannt im Gras einer Blumenwiese"></div>

  <section class="attitude">
    <h1 class="attitude-title">HALTUNG<br>An unserer Schule …</h1>
    <ul class="attitude-list">
      <li>… stehen die Lernenden im Mittelpunkt.</li>
      <li>… ist Integration selbstverständlich.</li>
      <li>… begegnen wir uns respektvoll und wertschätzend.</li>
      <li>… setzen wir uns für lebenslanges Lernen ein.</li>
    </ul>
  </section>

  <section class="section learning">
    <h2>LERNEN</h2>
    <ul>
      <li>Wir begleiten unsere Lernenden hin zur Selbständigkeit.</li>
      <li>Wir unterstützen individuellen Kompetenzerwerb.</li>
      <li>Wir ermöglichen allen Lernenden Erfolge.</li>
      <li>Die Unterrichtsinhalte orientieren sich an aktuellen Themen.</li>
      <li>Wir beurteilen transparent.</li>
      <li>Wir begegnen Heterogenität mit multiprofessionellen Teams.</li>
      <li>Wir schaffen eine wertschätzende und förderliche Atmosphäre.</li>
      <li>Unsere Schule bietet eine zeitgemässe Infrastruktur.</li>
    </ul>
  </section>

  <section class="section development">
    <h2>ENTWICKLUNG</h2>
    <ul>
      <li>Wir entwickeln unsere Schule gemeinsam.</li>
      <li>Wir setzen unsere Fähigkeiten und Kräfte gezielt ein.</li>
      <li>Alle tragen Verantwortung.</li>
      <li>Wir lernen alle voneinander.</li>
      <li>Wir bilden uns kontinuierlich weiter.</li>
      <li>Wir reflektieren unser Handeln.</li>
      <li>Wir sind innovativ und gehen mutig unseren Weg.</li>
    </ul>
  </section>

  <section class="section community">
    <h2>GEMEINSCHAFT</h2>
    <ul>
      <li>Unsere Schule achtet die Gesundheit aller.</li>
      <li>Wir legen Wert auf eine offene Kommunikation.</li>
      <li>Unsere pädagogische Zusammenarbeit basiert auf einer professionellen Haltung.</li>
      <li>Die Eltern sind ein Teil unserer Schulgemeinschaft und tragen Verantwortung.</li>
      <li>Wir haben an unserer Schule Freiräume innerhalb klarer Rahmenbedingungen.</li>
    </ul>
  </section>

  <address class="contact" style="font-style: normal;">
    <strong>Sekundarschule Talberg</strong><br>
    Lindenweg 12<br>
    4100 Talberg<br>
    Tel. 061 555 01 23<br>
    sekundarschule.talberg@sbt.ch
  </address>
  <div class="contact-bar"></div>
</main>
</body>
</html>
```